Stationery Design Project

We need a stationery design for a new business consulting business based in New Zealand.
We have the logo and business cards designed and we're looking for letterhead, compliments slip and PowerPoint presentation format that aligns with our business cards.
Industry/Entity Type
Business
Requirements
Must have
- same colors and format as business cards

```html
<!DOCTYPE html>
<html lang="en">
<head>
<meta charset="utf-8">
<title>Tussock Advisory – Compliments Slip</title>
<link rel="stylesheet" href="https://fonts.googleapis.com/css2?family=Arimo:wght@400;700&family=Pinyon+Script&display=swap">
<style>
  :root {
    --lime: #84ff0a;
    --slate: #95a0a0;
    --ink: #8a9494;
    --paper: #ffffff;
    --backdrop: #ffffff;
  }
  * { margin: 0; padding: 0; box-sizing: border-box; }
  html, body { width: 1200px; height: 1200px; overflow: hidden; background: var(--backdrop); }
  .canvas { position: relative; width: 1200px; height: 1200px; }

  .slip {
    position: absolute;
    left: 72px;
    width: 1050px;
    height: 500px;
    box-shadow: 0 1px 4px rgba(0,0,0,0.22);
  }
  .slip--front { top: 82px; background: var(--paper); }
  .slip--back { top: 622px; background: var(--lime); }

  .top-band {
    position: absolute; left: 573px; top: 0;
    width: 477px; height: 63px; background: var(--lime);
  }
  .side-band {
    position: absolute; left: 0; top: 254px;
    width: 60px; height: 246px; background: var(--slate);
  }

  .brand {
    position: absolute; left: 203px; top: 78px;
    display: flex; align-items: center; gap: 10px;
    font-family: "Arimo", Arial, sans-serif;
    font-weight: 400; font-size: 38px; letter-spacing: -0.5px;
    color: var(--ink);
  }
  .brand__mark { width: 18px; height: 18px; background: var(--lime); }

  .contact {
    position: absolute; left: 573px; top: 74px;
    font-family: "Arimo", Arial, sans-serif;
    font-weight: 700; font-size: 14.5px; line-height: 18.5px;
    color: var(--ink); list-style: none;
  }
  .contact li { display: flex; align-items: center; gap: 5px; }
  .contact svg { width: 13px; height: 13px; flex: none; }

  .greeting {
    position: absolute; left: 568px; top: 232px;
    font-family: "Pinyon Script", cursive;
    font-size: 66px; font-weight: 400; color: var(--lime);
    white-space: nowrap;
  }

  .botanical {
    position: absolute; left: 618px; top: 113px;
    width: 332px; height: 387px;
    background: radial-gradient(ellipse at 55% 70%, rgba(255,255,255,0.55), rgba(255,255,255,0.15) 60%, rgba(255,255,255,0) 80%);
  }
</style>
</head>
<body>
<div class="canvas">
  <section class="slip slip--front">
    <div class="top-band"></div>
    <div class="side-band"></div>

    <div class="brand">
      <span class="brand__mark"></span>
      <span class="brand__name">Tussock Advisory</span>
    </div>

    <ul class="contact">
      <li>PO Box 31907</li>
      <li>Hamilton 3204 New Zealand</li>
      <li>
        <svg viewBox="0 0 16 16" aria-hidden="true"><path d="M4 1.5 L6.5 5 L5 6.8 Q6.8 10 9.2 11 L11 9.5 L14.5 12 L13 14.5 Q6 14 1.5 3 Z" fill="#84ff0a"/></svg>
        + 64 21555014
      </li>
      <li>
        <svg viewBox="0 0 16 16" aria-hidden="true"><rect x="1.5" y="3.5" width="13" height="9" fill="none" stroke="#84ff0a" stroke-width="1.4"/><path d="M1.5 3.5 L8 9 L14.5 3.5" fill="none" stroke="#84ff0a" stroke-width="1.4"/></svg>
        enquiries@tussockadvisory.com
      </li>
      <li>
        <svg viewBox="0 0 16 16" aria-hidden="true"><circle cx="8" cy="8" r="6.3" fill="none" stroke="#84ff0a" stroke-width="1.3"/><ellipse cx="8" cy="8" rx="2.8" ry="6.3" fill="none" stroke="#84ff0a" stroke-width="1.1"/><path d="M1.8 8 H14.2 M2.8 4.8 H13.2 M2.8 11.2 H13.2" stroke="#84ff0a" stroke-width="1.1"/></svg>
        www.tussockadvisory.com
      </li>
    </ul>

    <p class="greeting">With compliments</p>
  </section>

  <section class="slip slip--back">
    <div class="botanical" role="img" aria-label="White line illustration of grasses and curling flower stems rising from the bottom edge"></div>
  </section>
</div>
</body>
</html>
```